Real-Estate business needs e-newsletter design for mail-chimp

We need a newsletter design as a PSD file.

Features of the e-newsletter design should include;

1. Our Corporate Colours and Logo - refer www.quellbrook.com.au
2. Our website menu items so readers can reference our services
3. Format should include our newsletter articles - usually 2 or 3 articles
4. Format should include a "special offer" section
5. Format should include our facebook likes widget as it appears on our website
6. Format should include company directors profile with "linked in" icon

```html
<!DOCTYPE html>
<html lang="en">
<head>
<meta charset="utf-8">
<title>Quellbrook Property Newsletter</title>
<link href="https://fonts.googleapis.com/css2?family=Questrial&family=Poiret+One&family=Josefin+Sans:wght@300;400&display=swap" rel="stylesheet">
<style>
  :root {
    --blue: #0b4a87;
    --charcoal: #262626;
    --silver: #9d9ea2;
    --mist: #a4a5a9;
    --white: #ffffff;
    --rule: #b8bcc4;
    --body-grey: #9a9a9a;
  }
  * { margin: 0; padding: 0; box-sizing: border-box; }
  html, body { width: 1028px; height: 1200px; overflow: hidden; background: var(--charcoal); }
  .newsletter { position: relative; width: 1028px; height: 1200px; font-family: "Questrial", sans-serif; }

  .masthead { position: absolute; left: 0; top: 0; width: 1028px; height: 85px; background: var(--blue); border-bottom: 3px solid var(--rule); }
  .brand { position: absolute; left: 40px; top: 24px; font-size: 31px; letter-spacing: 0.5px; color: var(--silver); text-transform: uppercase; font-weight: 400; }
  .top-links { position: absolute; right: 39px; top: 38px; display: flex; gap: 22px; font-size: 15px; color: var(--white); list-style: none; }

  .hero { position: absolute; left: 0; top: 88px; width: 1028px; height: 437px; background: var(--blue); overflow: hidden; }
  .hero-title { position: absolute; right: 31px; top: 110px; text-align: right; color: var(--silver); font-weight: 400; font-size: 40px; line-height: 49px; }
  .skyline { position: absolute; left: 0; top: 245px; width: 1028px; height: 112px; background: linear-gradient(to bottom, var(--blue) 0%, #1f3552 50%, var(--charcoal) 100%); }
  .nav-band { position: absolute; left: 0; top: 357px; width: 1028px; height: 80px; background: var(--charcoal); }
  .service-nav { list-style: none; font-size: 17px; color: var(--mist); text-transform: uppercase; }
  .service-nav li { position: absolute; top: 33px; }

  .offer { position: absolute; left: 0; top: 525px; width: 1028px; height: 301px; background: var(--mist); }
  .offer-illustration { position: absolute; left: 700px; top: 30px; width: 184px; height: 168px; background: linear-gradient(to bottom, var(--blue) 80%, rgba(11,74,135,0.55) 100%); }
  .offer-title { position: absolute; left: 170px; top: 118px; font-family: "Poiret One", sans-serif; font-weight: 400; font-size: 44px; line-height: 50px; color: var(--white); }
  .offer-call { position: absolute; left: 170px; top: 240px; font-family: "Questrial", sans-serif; font-size: 20px; color: var(--blue); }
  .offer-call .lead, .offer-call .phone { color: var(--white); }

  .articles { position: absolute; left: 0; top: 826px; width: 1028px; height: 328px; background: var(--charcoal); }
  .article { position: absolute; top: 59px; width: 266px; }
  .article-title { height: 43px; background: var(--blue); color: var(--white); font-family: "Josefin Sans", sans-serif; font-weight: 300; font-size: 16px; letter-spacing: -0.3px; line-height: 18px; display: flex; align-items: center; justify-content: center; text-align: center; padding: 0 2px; }
  .article-excerpt { height: 139px; padding: 22px 11px 0; font-family: "Josefin Sans", sans-serif; font-weight: 400; font-variant: small-caps; font-size: 14px; line-height: 20.5px; color: var(--body-grey); border-bottom: 1px solid var(--blue); }
  .read-more { display: block; text-align: right; padding: 7px 8px 0 0; font-family: "Josefin Sans", sans-serif; font-weight: 300; font-size: 17px; color: var(--white); }

  .footer { position: absolute; left: 0; top: 1154px; width: 1028px; height: 46px; background: var(--blue); }
  .footer-url { position: absolute; left: 0; width: 1028px; top: 13px; text-align: center; font-family: "Josefin Sans", sans-serif; font-weight: 300; font-size: 17px; color: var(--white); }
  .social { position: absolute; top: 15px; width: 17px; height: 17px; background: var(--silver); }
</style>
</head>
<body>
<div class="newsletter">
  <header class="masthead">
    <div class="brand">Quellbrook Property</div>
    <ul class="top-links">
      <li>ABOUT US</li><li>|</li><li>CONTACT US</li><li>|</li><li>LOGIN</li>
    </ul>
  </header>

  <section class="hero">
    <h1 class="hero-title">Let Us Help You......<br>SAVE MONEY &amp; REDUCE<br>RISK IN PROPERTY</h1>
    <div class="skyline" role="img" aria-label="City skyline silhouette with harbour bridge"></div>
    <nav class="nav-band">
      <ul class="service-nav">
        <li style="left:78px">Buyers Agent</li>
        <li style="left:263px">Property Advice</li>
        <li style="left:485px">Property Management</li>
        <li style="left:745px">Articles &amp; Resources</li>
      </ul>
    </nav>
  </section>

  <section class="offer">
    <div class="offer-illustration" role="img" aria-label="Blue house illustration"></div>
    <h2 class="offer-title">Free property<br>management for 2 months</h2>
    <p class="offer-call"><span class="lead">Call us today</span> to take advantage of our limited special offer on <span class="phone">1300 555 019</span></p>
  </section>

  <section class="articles">
    <article class="article" style="left:74px">
      <h3 class="article-title">The Property Investors Duty of Care</h3>
      <p class="article-excerpt">The recent deaths of five children in rental properties throughout the country has highlighted the need for a greater awareness of the maintenance required</p>
      <span class="read-more">Read more</span>
    </article>
    <article class="article" style="left:381px">
      <h3 class="article-title">Buying Well in a Hot Market</h3>
      <p class="article-excerpt">Investors shouldn't be lured in a false sense of security or a false economy in this market. The market will not keep going up indefinitely and interest rates</p>
      <span class="read-more">Read more</span>
    </article>
    <article class="article" style="left:688px">
      <h3 class="article-title">How did your Australian home<br>get its look.</h3>
      <p class="article-excerpt">Australian homes are made up of many different architectural styles? Have you ever wondered how the different styles came to be? What is your favorite?</p>
      <span class="read-more">Read more</span>
    </article>
  </section>

  <footer class="footer">
    <div class="footer-url">www.quellbrook.com.au</div>
    <span class="social" style="left:843px" aria-label="Professional network profile"></span>
    <span class="social" style="left:882px" aria-label="Social page"></span>
  </footer>
</div>
</body>
</html>
```